Coffee label for grocery store sales

We need a 3x4 label designed for our expanding grocery store market. I'm looking for something playful that will be eye catching on a shelf. Bag color is negotiable, but would prefer kraft, white, or black.

Target Market(s)

Grocery Stores

Industry/Entity Type

Coffee Shop

Logo Text

Heron Lane Coffee

Colors

Designer to choose colors to be used in the design.

Requirements
Must have
• Space for address label to identify blend.
• 47 W. Oak Ave., Dunmore, WI 54921
• www.heronlanecoffee.example
Nice to have
• Illustrations, bold colors

```html
<!DOCTYPE html>
<html lang="en">
<head>
<meta charset="utf-8">
<title>Heron Lane Coffee – Label</title>
<link rel="stylesheet" href="https://fonts.googleapis.com/css2?family=Oswald:wght@600;700&family=EB+Garamond:ital@1&display=swap">
<style>
  :root {
    --frame-brown: #6e4219;
    --gold-deep: #9c7a08;
    --gold-mid: #d6ad1c;
    --gold-light: #fbdf4f;
    --ink: #141414;
    --rule: #b48a12;
    --bean-dark: #2a1a10;
    --mascot-yellow: #f7d84a;
    --page: #ffffff;
  }
  html, body {
    margin: 0;
    padding: 0;
    width: 1200px;
    height: 1200px;
    overflow: hidden;
    background: var(--page);
  }
  .label {
    position: relative;
    width: 1200px;
    height: 1200px;
  }
  .label-art {
    position: absolute;
    inset: 0;
  }
  .brand-name,
  .brand-product {
    position: absolute;
    left: 0;
    right: 0;
    margin: 0;
    text-align: center;
    font-family: "Oswald", "Arial Narrow", sans-serif;
    font-weight: 700;
    font-variant: small-caps;
    color: var(--ink);
    line-height: 1;
    letter-spacing: 3px;
  }
  .brand-name {
    top: 338px;
    font-size: 118px;
  }
  .brand-product {
    top: 548px;
    font-size: 118px;
    letter-spacing: 5px;
  }
  .contact {
    position: absolute;
    left: 0;
    right: 0;
    margin: 0;
    text-align: center;
    font-family: "EB Garamond", Georgia, serif;
    font-style: italic;
    color: var(--ink);
    font-size: 40px;
    line-height: 1;
  }
  .contact-address { top: 695px; }
  .contact-web { top: 752px; }
</style>
</head>
<body>
<main class="label">
  <svg class="label-art" width="1200" height="1200" viewBox="0 0 1200 1200" xmlns="http://www.w3.org/2000/svg">
    <defs>
      <linearGradient id="gold-face" x1="0" y1="0" x2="1" y2="0">
        <stop offset="0" stop-color="var(--gold-deep)"/>
        <stop offset="0.45" stop-color="var(--gold-light)"/>
        <stop offset="0.75" stop-color="var(--gold-light)"/>
        <stop offset="1" stop-color="var(--gold-deep)"/>
      </linearGradient>
      <linearGradient id="bean-tones" x1="0" y1="0" x2="1" y2="0">
        <stop offset="0" stop-color="var(--gold-deep)"/>
        <stop offset="0.45" stop-color="var(--gold-mid)"/>
        <stop offset="0.55" stop-color="var(--bean-dark)"/>
        <stop offset="1" stop-color="var(--bean-dark)"/>
      </linearGradient>
    </defs>

    <path class="frame-outer" fill="var(--frame-brown)"
      d="M 40 225 Q 220 170 420 188 Q 555 200 600 148 Q 645 200 780 188 Q 980 170 1160 225
         Q 1175 400 1150 540 Q 1160 575 1188 595 Q 1160 615 1150 650
         Q 1180 850 1165 1000 Q 1000 990 860 1015 Q 700 1040 600 1030
         Q 500 1040 340 1015 Q 200 990 35 1000
         Q 20 850 50 650 Q 40 615 14 595 Q 40 575 50 540 Q 25 400 40 225 Z"/>

    <path class="frame-gold" fill="url(#gold-face)"
      d="M 95 262 Q 260 200 440 218 Q 560 228 600 200 Q 640 228 760 218 Q 940 200 1105 262
         Q 1140 420 1108 560 Q 1118 585 1132 595 Q 1118 605 1108 630
         Q 1140 820 1118 958 Q 980 955 850 968 Q 720 985 600 978
         Q 480 985 350 968 Q 220 955 82 958
         Q 60 820 92 630 Q 82 605 68 595 Q 82 585 92 560 Q 60 420 95 262 Z"/>

    <rect class="mascot" role="img" aria-label="Cartoon star mascot wearing sunglasses and giving two thumbs up"
      x="24" y="184" width="252" height="268" rx="40" fill="var(--mascot-yellow)"/>

    <rect class="crest" role="img" aria-label="Small illustration of two animal heads facing each other"
      x="472" y="468" width="252" height="64" rx="30" fill="#8a5a2a"/>

    <line class="divider" x1="292" y1="538" x2="910" y2="538" stroke="var(--rule)" stroke-width="5" stroke-linecap="round"/>

    <rect class="beans" role="img" aria-label="Illustration of two coffee beans, one golden and one dark roasted"
      x="492" y="812" width="360" height="220" rx="100" fill="url(#bean-tones)"/>
  </svg>

  <h1 class="brand-name">Heron Lane</h1>
  <p class="brand-product">Coffee</p>
  <p class="contact contact-address">47 W. Oak Ave., Dunmore, WI 54921</p>
  <p class="contact contact-web">www.heronlanecoffee.example</p>
</main>
</body>
</html>
```